Tavo's Spice Blend Dry Roasted and Freshly Ground Spices to create the Authentic and Aromatic Maur

I need a packaging design for a new company based in Kent called Tavo's Spice Blend. the size of the packaging will be for a 250gm bag.

I would like bright colours so that it can stand out from out the other products on a super market shelf

The packaging must have the list of ingredients on the back;

I.e. Ingredients;
Cumin
Coriander
Dried Red Chili
Cinnamon
Cloves
Cardamon
Black Peppercorn
Rice

Reason: Not enough designed to choose from. Tavo's Spice Blend, Dry Roasted and Freshly Ground Spices to create the Authentic and Aromatic flavour Please also add Turmeric to the ingredient list Thank you Bronna Castell

```html
<!DOCTYPE html>
<html lang="en">
<head>
<meta charset="utf-8">
<title>Tavo's Spice Blend – Curry Powder Pouch</title>
<link rel="stylesheet" href="https://fonts.googleapis.com/css2?family=Tenor+Sans&display=swap">
<style>
  :root {
    --page-bg: #f4f2f2;
    --pouch-red: #a8232d;
    --pouch-red-light: #c1454c;
    --pattern-red: #b8363e;
    --banner-dark: #4e0509;
    --banner-deep: #330204;
    --banner-pattern: #5f0b10;
    --accent-orange: #e07a3c;
    --text-light: #ffffff;
    --weight-text: #7a1a20;
  }
  * { margin: 0; padding: 0; box-sizing: border-box; }
  html, body {
    width: 1200px;
    height: 1200px;
    overflow: hidden;
    background: var(--page-bg);
  }
  .canvas {
    position: relative;
    width: 1200px;
    height: 1200px;
  }
  .pouch {
    position: absolute;
    left: 210px;
    top: 70px;
    width: 780px;
    height: 1060px;
    font-family: "Tenor Sans", sans-serif;
    color: var(--text-light);
  }
  .pouch-art {
    position: absolute;
    inset: 0;
    width: 780px;
    height: 1060px;
  }
  .brand-mark {
    position: absolute;
    left: 384px;
    top: 252px;
    width: 14px;
    height: 14px;
    border-radius: 50%;
    background: var(--text-light);
  }
  .brand-name {
    position: absolute;
    left: 157px;
    width: 495px;
    top: 345px;
    text-align: center;
    font-size: 116px;
    line-height: 1;
    color: var(--text-light);
  }
  .product-name {
    position: absolute;
    left: 157px;
    width: 495px;
    top: 512px;
    text-align: center;
    font-size: 37px;
    letter-spacing: 4px;
    line-height: 1;
  }
  .product-claim {
    position: absolute;
    left: 157px;
    width: 495px;
    top: 650px;
    text-align: center;
    font-size: 21px;
    line-height: 27px;
    letter-spacing: 3px;
    text-transform: uppercase;
  }
  .net-weight {
    position: absolute;
    left: 0;
    width: 780px;
    top: 1034px;
    text-align: center;
    font-size: 16px;
    letter-spacing: 2px;
    color: var(--weight-text);
  }
</style>
</head>
<body>
<main class="canvas">
  <section class="pouch">
    <svg class="pouch-art" viewBox="0 0 780 1060" aria-hidden="false">
      <defs>
        <linearGradient id="bannerShade" x1="0" y1="0" x2="0" y2="1">
          <stop offset="0" stop-color="var(--banner-deep)"/>
          <stop offset="1" stop-color="var(--banner-dark)"/>
        </linearGradient>
      </defs>
      <!-- pouch base -->
      <rect class="pouch-base" x="0" y="0" width="780" height="1060" fill="var(--pouch-red)"/>
      <!-- orange arc band -->
      <path class="accent-arc" d="M0 330 Q90 270 157 262 L157 290 Q90 298 0 360 Z" fill="var(--accent-orange)"/>
      <path class="accent-arc" d="M780 330 Q690 270 652 262 L652 290 Q690 298 780 360 Z" fill="var(--accent-orange)"/>
      <!-- mandala pattern field -->
      <path class="pattern-field" role="img" aria-label="Decorative mandala and paisley pattern in soft red tones"
            d="M0 360 Q90 298 157 290 L652 290 Q690 298 780 360 L780 1060 L0 1060 Z"
            fill="var(--pattern-red)"/>
      <!-- central banner -->
      <path class="banner" d="M157 0 L652 0 L652 968 L404 850 L157 968 Z" fill="url(#bannerShade)"/>
      <path class="banner-pattern" role="img" aria-label="Dark mandala pattern within the banner"
            d="M157 360 Q280 300 404 330 Q528 300 652 360 L652 968 L404 850 L157 968 Z"
            fill="var(--banner-pattern)"/>
      <!-- stitched borders -->
      <path class="stitch-line" d="M172 0 L172 945 L404 834 L637 945 L637 0"
            fill="none" stroke="var(--text-light)" stroke-width="2.5" stroke-dasharray="6 6"/>
    </svg>
    <span class="brand-mark"></span>
    <h1 class="brand-name">Tavo's</h1>
    <h2 class="product-name">CURRY POWDER</h2>
    <p class="product-claim">Dry roasted<br>freshly ground<br>spices to create the<br>authentic and<br>aromatic maur</p>
    <p class="net-weight">250g net weight</p>
  </section>
</main>
</body>
</html>
```